依頼詳細
両面フルカラーでお願いします。

【表】
SEOやコンサルタントといった自分の知識を商材としますので、誠実さが伝わるデザインを希望します。ただ、誠実すぎて硬すぎるデザインではなくスタイリッシュなデザインになるようにしてください。

【裏】
将来の展望として大学生など若い世代や企業といった様々な人との関わりを持ちたいと考えております。幅広い世代にウケる遊び心のあるデザインをお願いします。

【ロゴについて】
ロゴのデザインは人と企業と弊社がつながっているロゴになっています。
名刺でも人のつながりと拡散が伝わるようなデザインになれればお願いします。
記載項目
表面:会社名/役職/名前/住所/電話/FAX/携帯番号/Mail/URL
裏面:社名(ロゴ可)/名前
希望イメージ
シンプル 複雑
単色 カラフル
暗い 明るい
日常 高級
遊び心 厳粛
未来的 伝統的
女性的 男性的
希望する色
お任せします。
納品ファイル
• イラストレーター形式 (.ai)
• フォトショップ形式 (.psd)
• PNG形式 (.png)
補足説明
自社サービスなどができてくると、背面デザインを変える事になると思います。そうなった時には都度お仕事を依頼できればと思います。
大変失礼いたしました。
会社名が抜けておりました。

登記する会社名は「株式会社ブライトピーク」となります。
ただ、株式会社にするか合同にするかまだ本決定していないので後で変更をお願いするかもしれません。

提案書などのコピーライトで使う会社名は「BRIGHTPEAK」となります。
デザイン表現のなかで英語表記がしっくりくるようでしたら英語表記でも問題ありません。
ロゴ画像が添付できていなかったようですので添付いたします。
失礼いたしました。
ロゴaiデータのバージョンを落としました。
CS2に落とすことと、PDF変換を付けましたので、現在掲載しているロゴデータが開けられない方はこちらをご利用ください。

変換ファイル

よろしくお願いいたします。
選定確約を付けさせていただきました。

また、ロゴの提供が遅れてしまったことや土日をまたいで、より多くのご提案を言頂きたいと思いましたので、期間を延長させていただきました。

まだまだ、ご提案をお待ちしておりますので、
ご提案いただいた方も、今やられている方も、引き続きよろしくお願いいたします。
■ 選んだ理由

表面の配置がとても綺麗でまとまりがありましたので、こちらのデザインとさせていただきました。

■ 提案者全員のお礼・コメント

多くのご提案本当にありがとうございました。どれも良いデザインで全て使わせていただきたいくらいだったのですが、社員に聞いてみて全体で決めさせていただきました。選ばれなかった方も選ばれた方もとてもユニークなアイデアを下さりありがとうございました。

```html
<!DOCTYPE html>
<html lang="ja">
<head>
<meta charset="utf-8">
<title>BRIGHT PEAK 名刺デザイン</title>
<link href="https://fonts.googleapis.com/css2?family=Noto+Sans+JP:wght@400;500;700&family=Noto+Serif:ital,wght@0,400&display=swap" rel="stylesheet">
<style>
  :root {
    --navy: #15306f;
    --blue-deep: #1c3d8f;
    --blue-mid: #3a62b8;
    --blue-pale: #cfdaef;
    --line-blue: #2b4fa3;
    --gold: #e9b422;
    --ink: #222;
    --paper: #ffffff;
  }
  * { margin: 0; padding: 0; box-sizing: border-box; }
  html, body { width: 797px; height: 1200px; overflow: hidden; background: var(--paper); }
  body { position: relative; font-family: "Noto Sans JP", sans-serif; color: var(--ink); }

  .side-label { position: absolute; left: 106px; font-size: 22px; font-weight: 700; }
  .side-label.front { top: 92px; }
  .side-label.back { top: 636px; }

  .card {
    position: absolute; left: 106px; width: 590px; height: 380px; overflow: hidden;
    box-shadow: 3px 4px 8px rgba(0,0,0,.35);
  }
  .card.front {
    top: 165px;
    background: linear-gradient(135deg, var(--blue-deep) 0%, var(--blue-mid) 48%, var(--blue-pale) 100%);
  }
  .cube-field {
    position: absolute; left: 0; top: 0; width: 420px; height: 380px;
    background: linear-gradient(150deg, rgba(255,255,255,.18) 0%, rgba(255,255,255,.05) 45%, rgba(255,255,255,.35) 100%);
  }
  .brand-tagline { position: absolute; left: 400px; top: 36px; font-size: 10px; color: #fff; letter-spacing: .03em; }
  .brand {
    position: absolute; display: flex; align-items: center; gap: 12px;
    font-weight: 700; letter-spacing: .06em;
  }
  .brand .dot { border-radius: 50%; background: var(--gold); flex: none; }
  .front .brand { left: 335px; top: 64px; color: #fff; font-size: 34px; }
  .front .brand .dot { width: 42px; height: 42px; }
  .motto { position: absolute; left: 58px; top: 122px; font-family: "Noto Serif", serif; font-size: 15px; color: #fff; }

  .slant {
    position: absolute; left: 130px; top: 170px; transform: rotate(32deg); transform-origin: left top;
    color: var(--navy); font-size: 14px; line-height: 30px;
  }
  .slant p:nth-child(1) { margin-left: 40px; }
  .slant p:nth-child(2) { margin-left: 10px; }
  .slant p:nth-child(3) { margin-left: -30px; font-size: 16px; }

  .card.back {
    top: 704px;
    background: linear-gradient(160deg, #ffffff 0%, #eef2f9 60%, #dfe6f3 100%);
  }
  .back svg.frame { position: absolute; left: 0; top: 0; }
  .back .brand { left: 28px; top: 66px; color: var(--line-blue); font-size: 22px; gap: 8px; }
  .back .brand .dot { width: 22px; height: 22px; }
  .role { position: absolute; left: 262px; top: 152px; font-size: 11px; }
  .name { position: absolute; left: 408px; top: 136px; font-size: 30px; font-weight: 500; letter-spacing: .08em; }
  .reading { position: absolute; left: 412px; top: 180px; font-size: 8px; color: #666; word-spacing: 26px; }
  .mobile { position: absolute; left: 92px; top: 226px; font-size: 11px; }
  .band { position: absolute; left: 0; top: 262px; }
  .contact { position: absolute; left: 70px; top: 292px; color: #fff; font-size: 11.5px; line-height: 20px; }
  .contact .company { font-size: 15px; font-weight: 700; margin-right: 14px; }
</style>
</head>
<body>
  <div class="side-label front">表面</div>
  <section class="card front">
    <div class="cube-field" role="img" aria-label="重なり合う立方体のパターン"></div>
    <p class="brand-tagline">Network Intellect creator</p>
    <div class="brand"><span class="dot"></span>BRIGHT PEAK</div>
    <p class="motto">The route to the future is not one</p>
    <div class="slant">
      <p>Tel : 03-0000-0000</p>
      <p>http://www.brightpeak.jp</p>
      <p>株式会社ブライトピーク</p>
    </div>
  </section>

  <div class="side-label back">裏面</div>
  <section class="card back">
    <svg class="frame" width="590" height="262" viewBox="0 0 590 262">
      <g stroke="var(--line-blue)" stroke-width="1.5" fill="none">
        <line x1="385" y1="0" x2="385" y2="62"/>
        <line x1="385" y1="62" x2="545" y2="62"/>
        <line x1="545" y1="0" x2="545" y2="246"/>
        <line x1="70" y1="246" x2="545" y2="246"/>
      </g>
      <g fill="var(--line-blue)">
        <circle cx="385" cy="62" r="4.5"/>
        <circle cx="545" cy="62" r="4.5"/>
        <circle cx="545" cy="246" r="4.5"/>
      </g>
    </svg>
    <div class="brand"><span class="dot"></span>BRIGHT PEAK</div>
    <p class="role">代表取締役／CEO</p>
    <p class="name">山田 健</p>
    <p class="reading">Yamada Ken</p>
    <p class="mobile">mobile phone : 0000-0000-00000</p>
    <svg class="band" width="590" height="124" viewBox="0 0 590 124">
      <path d="M0 14 C150 -6 300 34 430 14 C500 4 560 6 590 12 L590 124 L0 124 Z" fill="var(--line-blue)"/>
      <path d="M0 8 C160 -8 300 28 440 8 C510 0 560 2 590 6" fill="none" stroke="#8fa7d8" stroke-width="1.5"/>
    </svg>
    <div class="contact">
      <p><span class="company">株式会社ブライトピーク</span>〒000-0000 東京都港区南青山0-0-0</p>
      <p>TEL : 03-0000-0000　FAX : 03-0000-0000　e-mail : info@brightpeak.jp</p>
      <p>URL : http://www.brightpeak.jp</p>
    </div>
  </section>
</body>
</html>
```